Larkspur Ridge Management - Business Cards

I need business cards. My current logo was designed by a designer at this site and I very much like and am happy with the results. I would like a business card that is trendy, unique, current yet professional. I deal with high net worth clients daily

Target Market(s)

Out of state investors looking to get into the rental market in Ohio

Industry/Entity Type

Property Management, Consulting

Contact Information for Business Card

Name, Title (Chief Financial Officer) office phone number (555) 817-3094 website address larkridgemgmt.example

Font styles to use
Sans Serif

Colors
0054AA
0677BA
7BADD7
CADEEF
E8F1F8
0094D4
00A9DD
6FCCEA
C7EBF8
E9F6FB
00AB8E
00BBA5
67D7C9
C6EFE9
E9F9F6

```html
<!DOCTYPE html>
<html lang="en">
<head>
<meta charset="utf-8">
<title>Larkspur Ridge Management – Business Cards</title>
<link rel="stylesheet" href="https://fonts.googleapis.com/css2?family=Merriweather:wght@400;700&family=Roboto:wght@400&display=swap">
<style>
  :root {
    --stage-light: #e4e5e6;
    --stage-dark: #cfd0d1;
    --ink: #111418;
    --white: #ffffff;
    --navy: #1f3560;
    --blue-deep: #1453a8;
    --blue-mid: #0677ba;
    --sky: #00a9dd;
    --teal: #00bba5;
    --violet: #7a64c0;
    --icon-blue: #1b5fb4;
  }
  * { box-sizing: border-box; margin: 0; padding: 0; }
  html, body { width: 1200px; height: 675px; overflow: hidden; }
  body {
    position: relative;
    background: linear-gradient(90deg, var(--stage-light) 0%, #dcdddf 50%, var(--stage-dark) 100%);
    font-family: "Merriweather", Georgia, serif;
  }
  .side-label {
    position: absolute;
    font-family: "Roboto", Arial, sans-serif;
    font-size: 50px;
    line-height: 1;
    color: var(--ink);
  }
  .side-label--front { left: 856px; top: 258px; }
  .side-label--back { left: 171px; top: 601px; }

  .card {
    position: absolute;
    left: 308px;
    width: 514px;
    height: 294px;
    overflow: hidden;
  }
  .card--front { top: 35px; }
  .card--back { top: 352px; background: var(--white); }

  .skyline-photo {
    position: absolute;
    inset: 0;
    background:
      radial-gradient(ellipse 60% 40% at 35% 40%, rgba(255,255,255,0.35), transparent 70%),
      linear-gradient(180deg, rgba(40,60,140,0.35) 0%, transparent 40%, rgba(90,80,170,0.25) 100%),
      linear-gradient(120deg, var(--violet) 0%, #5a78cc 35%, #1a96d6 65%, #1fb59a 100%);
  }
  .front-brand {
    position: absolute;
    left: 268px;
    top: 88px;
    width: 190px;
    display: flex;
    align-items: center;
    gap: 10px;
  }
  .front-brand__mark {
    flex: none;
    width: 26px; height: 26px;
    border-radius: 50%;
    background: var(--navy);
  }
  .front-brand__name {
    color: var(--white);
    font-weight: 700;
    font-size: 22px;
    line-height: 1.25;
  }

  .back-brand {
    position: absolute;
    left: 45px;
    top: 40px;
    width: 140px;
    color: var(--navy);
    font-weight: 700;
    font-size: 14px;
    line-height: 1.3;
  }
  .contact {
    position: absolute;
    right: 53px;
    top: 122px;
    text-align: right;
    color: var(--ink);
  }
  .contact__name { font-size: 27px; line-height: 34px; font-weight: 400; }
  .contact__title { font-size: 13px; line-height: 18px; margin-top: 4px; }
  .contact__line {
    display: flex;
    justify-content: flex-end;
    align-items: center;
    gap: 5px;
    font-size: 13px;
    line-height: 18px;
  }
  .contact__line--phone { margin-top: 12px; }
  .contact__line--web { margin-top: 10px; }
  .contact__icon { width: 14px; height: 14px; flex: none; }
  .back-band {
    position: absolute;
    left: 0; bottom: 0;
    width: 100%; height: 38px;
    background: linear-gradient(90deg, var(--blue-deep) 0%, var(--blue-mid) 55%, #20a9cc 100%);
  }
</style>
</head>
<body>
  <section class="card card--front">
    <div class="skyline-photo" role="img" aria-label="City skyline photograph across the river with blue-violet to teal colour wash"></div>
    <div class="front-brand">
      <span class="front-brand__mark"></span>
      <span class="front-brand__name">Larkspur Ridge Management</span>
    </div>
  </section>
  <span class="side-label side-label--front">Front</span>

  <section class="card card--back">
    <div class="back-brand">Larkspur Ridge Management</div>
    <div class="contact">
      <h1 class="contact__name">Name</h1>
      <p class="contact__title">Chief Financial Officer</p>
      <p class="contact__line contact__line--phone">
        <span>(555) 817-3094</span>
        <svg class="contact__icon" viewBox="0 0 24 24" aria-hidden="true"><path fill="var(--icon-blue)" d="M6.6 10.8a15.1 15.1 0 0 0 6.6 6.6l2.2-2.2c.3-.3.7-.4 1-.2 1.1.4 2.3.6 3.6.6.6 0 1 .4 1 1V20c0 .6-.4 1-1 1A17 17 0 0 1 3 4c0-.6.4-1 1-1h3.5c.6 0 1 .4 1 1 0 1.3.2 2.5.6 3.6.1.3 0 .7-.2 1z"/></svg>
      </p>
      <p class="contact__line contact__line--web">
        <span>www.larkridgemgmt.example</span>
        <svg class="contact__icon" viewBox="0 0 24 24" aria-hidden="true" fill="none" stroke="var(--icon-blue)" stroke-width="1.6"><circle cx="12" cy="12" r="10"/><ellipse cx="12" cy="12" rx="4.5" ry="10"/><path d="M2 12h20M4 7h16M4 17h16M12 2v20"/></svg>
      </p>
    </div>
    <div class="back-band"></div>
  </section>
  <span class="side-label side-label--back">Back</span>
</body>
</html>
```